Womens Personal Training studio needs new year flyers

I need a double sided A5 flyer to attract Women / Mothers to my fitness business, Radiant Core Studio, in the new year.

My business colour is teal, I am located in Oakvale QLD Aus

Exclusive studio training for women. At Radiant Core Studio we don't make New years resolutions, we Empower you to make the changes for life!

examples of pain Q's: Do you feel guilty about wanting to do something for yourself? Do you worry about what exercises are safe post baby? Are you struggling to regain control of your body and your life?

Would you like to love yourself and your body as much as you lvoe your baby?

I work with women to apporpriately and progressivley rebuild their bodies post preganany. As the Leading specialist in Pre and Post Natal Rehabilitation and Fitness in Durnford, Marnie knows what it takes to find the right balance. With a vision of Empowering this generation to inspire the next, Marnie teaches skills for LIFE so you can lead your family to a Healthier, Fitter and Stronger future! Using a fusion of Pilates, Strength Conditioning and Cardio Marnie customises a plan for each individual. Your free consultation is waiting call now and learn the first steps to making the change Valued at $147 Don’t Miss out!! Marnie 0438 270 614

Quote to go with image "Marnie doesn't just help you achieve your weight loss goals she works with you to make sure you are 'Radiant Core Studio'." Tessa Brook July 2013

Target Market(s)

Women / Mothers

Industry/Entity Type

Training

Requirements
Must have
• call to action
contact details
Marnie Clarke
0438 270 614
marnie@radiantcorestudio.net.au
www.radiantcorestudio.net.au

```html
<!DOCTYPE html>
<html lang="en">
<head>
<meta charset="utf-8">
<title>Radiant Core Studio – New Year Flyer</title>
<link href="https://fonts.googleapis.com/css2?family=Mulish:wght@300;400;700;800&family=Nunito:wght@800;900&display=swap" rel="stylesheet">
<style>
  :root {
    --stage: #202020;
    --teal-deep: #1b6a6e;
    --teal: #2a9496;
    --teal-soft: #9fd3d3;
    --pink: #ee6fb4;
    --pink-soft: #f2a9d2;
    --white: #ffffff;
    --ink: #2b3a3a;
  }
  * { margin: 0; padding: 0; box-sizing: border-box; }
  html, body { width: 1200px; height: 1000px; overflow: hidden; }
  body { background: var(--stage); font-family: "Mulish", sans-serif; position: relative; }

  .flyer-front, .flyer-back { position: absolute; top: 94px; height: 790px; overflow: hidden; }

  /* Front side */
  .flyer-front {
    left: 42px; width: 560px;
    background: linear-gradient(180deg, #175f63 0%, #2b8587 22%, #8ec9c9 40%, #cfe8e8 100%);
  }
  .front-photo {
    position: absolute; left: 0; top: 200px; width: 560px; height: 590px;
    background:
      linear-gradient(180deg, rgba(43,133,135,0.9) 0%, rgba(43,133,135,0) 22%),
      linear-gradient(90deg, #e9d6cf 0%, #e6c2ad 45%, #c99a80 75%, #b6d9d8 100%);
  }
  .pain-questions { position: absolute; left: 48px; top: 35px; font-size: 14px; font-weight: 700; line-height: 17px; }
  .pain-questions .q-pink { color: var(--pink-soft); }
  .pain-questions .q-teal { color: var(--teal-soft); }
  .front-headline {
    position: absolute; left: 46px; top: 78px; width: 500px;
    color: var(--white); font-size: 37px; font-weight: 300; line-height: 40px;
  }
  .front-headline b { font-weight: 800; }
  .front-brand { position: absolute; right: 12px; bottom: 36px; color: var(--white); font-size: 18px; font-weight: 400; }

  /* Back side */
  .flyer-back {
    left: 612px; width: 548px;
    background: linear-gradient(180deg, #9fd2d3 0%, #e6f3f3 14%, #f6dbe3 32%, #ffffff 52%, #f3f9f9 74%, #8ecdcd 100%);
  }
  .back-headline {
    position: absolute; left: 51px; top: 54px; width: 490px;
    color: var(--teal); font-size: 27px; font-weight: 300; line-height: 34px; white-space: nowrap;
  }
  .back-headline b { font-weight: 800; }
  .back-body {
    position: absolute; left: 51px; top: 206px; width: 466px;
    color: var(--ink); font-size: 11.4px; line-height: 18.5px;
  }
  .back-cta {
    position: absolute; left: 51px; top: 334px; width: 480px; white-space: nowrap;
    font-family: "Nunito", sans-serif; font-weight: 900; font-size: 17.5px; line-height: 20px;
    color: var(--teal); letter-spacing: 1px;
  }
  .back-cta .accent { color: var(--pink); }
  .progress-photos {
    position: absolute; left: 42px; top: 440px; width: 150px; height: 222px;
    background: linear-gradient(180deg, #eef6f6 0%, #e4eeee 60%, #d3e6e6 100%);
  }
  .progress-label { position: absolute; top: 666px; color: var(--pink-soft); font-size: 15px; }
  .progress-label.before { left: 58px; }
  .progress-label.after { left: 135px; }
  .testimonial {
    position: absolute; left: 206px; top: 447px; width: 310px; white-space: nowrap;
    font-family: "Nunito", sans-serif; font-weight: 800; font-size: 19.5px; line-height: 25.5px;
    letter-spacing: 0.6px; color: var(--pink);
  }
  .testimonial b { font-weight: 900; }
  .testimonial-cite { position: absolute; left: 208px; top: 592px; color: var(--teal); font-size: 13px; font-style: normal; font-weight: 300; }
  .back-brand { position: absolute; left: 231px; top: 656px; color: var(--teal); font-size: 26px; font-weight: 400; }
  .back-contact { position: absolute; right: 38px; top: 710px; text-align: right; color: var(--teal); font-size: 15px; line-height: 20px; font-style: normal; font-weight: 300; }
</style>
</head>
<body>

<section class="flyer-front">
  <div class="front-photo" role="img" aria-label="Photograph of a smiling mother kissing her baby's cheek"></div>
  <p class="pain-questions">
    <span class="q-pink">Do you feel guilty about wanting to do something for yourself?</span><br>
    <span class="q-teal">Are you struggling to regain control of your body and your life?</span>
  </p>
  <h1 class="front-headline">Would you like to love <b>your body</b> and <b>your life</b> as much as you love <b>your baby</b>?</h1>
  <div class="front-brand">Radiant Core Studio</div>
</section>

<section class="flyer-back">
  <h2 class="back-headline"><b>Exclusive</b> studio training for women.<br>At <b>Radiant Core Studio</b> we don't make<br>New year's resolutions, we <b>Empower</b><br>you to make the changes for life!</h2>
  <p class="back-body">As the leading specialist in Pre and Post Natal Rehabilitation and Fitness in Durnford, Marnie knows what it takes to find the right balance while appropriately and progressivley rebuilding the body post pregnancy. Using a fusion of Pilates, Strength Conditioning and Cardio Marnie customises a plan for each individual. With a vision of Empowering this generation to inspire the next, Marnie teaches you skills for LIFE so you can lead your family to a healthier, fitter and stronger future!</p>
  <p class="back-cta">Your <span class="accent">free consultation</span> is waiting. Call now<br>and learn the first steps to making the<br>change valued at $147. Don't Miss out!!<br>Marnie 0438 270 614</p>

  <div class="progress-photos" role="img" aria-label="Before and after profile photographs of a client, pregnant and post pregnancy"></div>
  <span class="progress-label before">before</span>
  <span class="progress-label after">after</span>

  <blockquote class="testimonial">"Marnie doesn't just help<br>you achieve your weight<br>loss goals she works with<br>you to make sure you are<br>'<b>Radiant Core Studio</b>'."</blockquote>
  <cite class="testimonial-cite">Tessa Brook, July 2013</cite>

  <div class="back-brand">Radiant Core Studio</div>
  <address class="back-contact">
    Marnie Clarke: 0438 270 614 marnie@radiantcorestudio.net.au<br>
    www.radiantcorestudio.net.au
  </address>
</section>

</body>
</html>
```